Presentation Folder Cover For Plumbing Company

We need a presentation folder cover (FRONT AND BACK) for our plumbing business.

We specialise in plumbing, hot water, electrical and pipe relining.

This will be sent to clients and the contents pages will outline all of our company details and information.

The target market for this cover is Strata / Property Managers who look after unit buildings.

Target Market(s)

Strata & Property Managers. The higher end of the property market.

Industry/Entity Type

Plumbing

Font styles to use
Sans Serif

Colors
ec1f27
0355a3
ffffff
474747
c9c9c9

Requirements
Must have
• A4 Paper Size
• Inviting to clients to open the document and read on.
Nice to have
• Sleek, Professional and Stands Out.
Should not have
• Dark Background. Needs to be fresh and bright.

```html
<!DOCTYPE html>
<html lang="en">
<head>
<meta charset="utf-8">
<title>Crest Contracting – Presentation Folder</title>
<link href="https://fonts.googleapis.com/css2?family=Montserrat:wght@400;500;600;700;800&family=Oswald:wght@600&display=swap" rel="stylesheet">
<style>
  :root{
    --red:#ec1f27;
    --blue:#0355a3;
    --blue-mid:#3f7fbf;
    --blue-light:#a9c8e8;
    --blue-pale:#dbe8f5;
    --white:#ffffff;
    --ink:#1c1c1c;
    --grey-dark:#474747;
    --grey:#c9c9c9;
    --bg:#d9d9d9;
  }
  *{margin:0;padding:0;box-sizing:border-box}
  html,body{width:1200px;height:809px;overflow:hidden;background:var(--bg)}
  body{font-family:"Montserrat",Arial,sans-serif;color:var(--grey-dark)}
  .spread{position:absolute;left:60px;top:22px;width:1080px;height:764px;display:flex}
  .panel{position:relative;width:540px;height:764px;overflow:hidden;background:linear-gradient(160deg,#fdfdfd,#f2f2f2)}
  .panel--back{border-right:1px solid #e2e2e2}
  .panel svg.deco{position:absolute;inset:0}

  /* back */
  .back-photo{position:absolute;left:20px;top:120px;width:380px;height:280px;border-radius:40px;
    background:linear-gradient(135deg,#ececec,#f7f7f7 60%,#efefef);opacity:.9}
  .seal{position:absolute;left:150px;top:410px;width:240px;height:240px;border-radius:50%;
    background:var(--white);box-shadow:0 0 0 6px #f0f0f0;display:flex;flex-direction:column;align-items:center;justify-content:center}
  .brand-name{font-weight:800;color:var(--blue);line-height:1.05;text-align:center}
  .seal .brand-name{font-size:26px}
  .seal .trades{font-size:10px;font-weight:700;color:var(--ink);margin-top:8px}
  .contact{position:absolute;left:40px;bottom:60px}
  .contact h3{color:var(--red);font-size:17px;font-weight:700;margin-bottom:10px;border-bottom:2px solid var(--red);display:inline-block;padding-bottom:1px}
  .contact li{list-style:none;display:flex;align-items:center;gap:10px;font-size:13px;color:var(--grey-dark);margin:6px 0}
  .contact svg{width:18px;height:18px;flex:none}
  .follow{position:absolute;right:30px;bottom:150px;display:flex;align-items:center;gap:6px;font-size:13px;color:var(--grey-dark)}
  .follow .dot{width:20px;height:20px;border-radius:50%;background:var(--red)}
  .base-line{position:absolute;left:0;right:0;bottom:0;height:6px;background:var(--red)}

  /* front */
  .hero-photo{position:absolute;left:210px;top:-70px;width:420px;height:420px;border-radius:50%;
    background:radial-gradient(circle at 40% 40%,#f4f4f4,#bdbdbd 55%,#8a8a8a)}
  .front-brand{position:absolute;left:0;right:0;top:448px;text-align:center}
  .front-brand .brand-name{font-size:38px}
  .front-brand .trades{font-size:14px;font-weight:700;color:var(--ink);margin-top:10px}
  .callout{position:absolute;left:0;right:0;top:580px;text-align:center}
  .callout p{font-size:15px;color:var(--ink);font-weight:500}
  .callout h2{font-family:"Oswald",Impact,sans-serif;font-weight:600;font-size:31px;line-height:1.3;color:var(--ink);letter-spacing:.5px;margin-top:2px}
  .callout h2 span{color:var(--red)}
  .callout .web{font-size:11px;letter-spacing:5px;color:var(--grey-dark);margin-top:10px}
  .front-stripe{position:absolute;left:0;right:0;bottom:0;height:16px}
  .front-stripe .blue{position:absolute;right:0;bottom:0;width:100%;height:10px;background:var(--blue)}
  .front-stripe .red{position:absolute;left:0;bottom:10px;width:100%;height:3px;background:var(--red)}
</style>
</head>
<body>
<main class="spread">

  <section class="panel panel--back" aria-label="Folder back">
    <div class="back-photo" role="img" aria-label="Faint photograph of a chrome mixer tap"></div>
    <svg class="deco" width="540" height="764" aria-hidden="true">
      <circle cx="430" cy="70" r="90" fill="#e6e6e6"/>
      <circle cx="430" cy="70" r="70" fill="none" stroke="#fafafa" stroke-width="10"/>
      <circle cx="500" cy="310" r="24" fill="#e2e2e2"/>
      <circle cx="440" cy="440" r="55" fill="#ececec"/>
      <circle cx="40" cy="580" r="26" fill="#e4e4e4"/>
    </svg>
    <div class="seal">
      <div class="brand-name">CREST<br>Contracting</div>
      <div class="trades">Plumbing • Electrical • Hot Water</div>
    </div>
    <div class="follow">follow us : <span class="dot"></span><span class="dot"></span></div>
    <div class="contact">
      <h3>Get in Touch</h3>
      <ul>
        <li><svg viewBox="0 0 18 18"><circle cx="9" cy="9" r="9" fill="#ec1f27"/><path d="M9 4a3 3 0 0 0-3 3c0 2.3 3 6 3 6s3-3.7 3-6a3 3 0 0 0-3-3z" fill="#fff"/><circle cx="9" cy="7" r="1" fill="#ec1f27"/></svg>Address Goes Here</li>
        <li><svg viewBox="0 0 18 18"><circle cx="9" cy="9" r="9" fill="#ec1f27"/><path d="M6 5l2 2-1 1.2a6 6 0 0 0 2.8 2.8L11 10l2 2-1.3 1.3C9 13 5 9 4.7 6.3z" fill="#fff"/></svg>0123 456 789</li>
        <li><svg viewBox="0 0 18 18"><circle cx="9" cy="9" r="9" fill="#ec1f27"/><rect x="4.5" y="6" width="9" height="6" fill="#fff"/><path d="M4.5 6l4.5 3.5L13.5 6" stroke="#ec1f27" fill="none"/></svg>info@crestcontracting.example</li>
        <li><svg viewBox="0 0 18 18"><circle cx="9" cy="9" r="9" fill="#ec1f27"/><circle cx="9" cy="9" r="4.5" fill="none" stroke="#fff"/><path d="M4.5 9h9M9 4.5v9" stroke="#fff"/></svg>www.crestcontracting.example</li>
      </ul>
    </div>
    <div class="base-line"></div>
  </section>

  <section class="panel panel--front" aria-label="Folder front">
    <svg class="deco" width="540" height="764" aria-hidden="true">
      <circle cx="100" cy="250" r="62" fill="var(--blue-pale)"/>
      <circle cx="110" cy="345" r="20" fill="var(--blue-pale)"/>
      <circle cx="490" cy="395" r="40" fill="#eef3f9"/>
      <path d="M258 -50 A250 250 0 0 0 540 359" fill="none" stroke="var(--blue)" stroke-width="30"/>
      <path d="M305 -50 A222 222 0 0 0 540 327" fill="none" stroke="var(--blue-light)" stroke-width="14"/>
      <path d="M152 110 A270 270 0 0 0 540 382" fill="none" stroke="var(--blue-mid)" stroke-width="5"/>
    </svg>
    <div class="hero-photo" role="img" aria-label="Photograph of a chrome basin tap over a white sink"></div>
    <div class="front-brand">
      <div class="brand-name">CREST<br>Contracting</div>
      <div class="trades">Plumbing • Electrical • Hot Water</div>
    </div>
    <div class="callout">
      <p>Call 1 Number for The Best in 3 Trades</p>
      <h2>PLUMBING, <span>HOT WATER &amp; ELECTRICAL</span></h2>
      <div class="web">www.crestcontracting.example</div>
    </div>
    <div class="front-stripe"><div class="red"></div><div class="blue"></div></div>
  </section>

</main>
</body>
</html>
```